Catchy Cards for Hospital

I run a rural hospital in Texas called Pellor Valley Hospital and am in need of contemporary business cards for all of my Department Heads. While our logo is somewhat simplistic, I don't have the option of changing it at this time, so anything to make the rest of the card present the appearance of a modern, professional healthcare facility would be great. Although the attached files are in black, our hospital colors are in a copper brown and black. I need to be able to change the name and title on the card so I can get cards printed for various department heads.

Target Market(s)

Referring physicians, large hospital systems, national organizations, state and federal government

Industry/Entity Type

Hospital

Contact Information for Business Card

Name Dale Hoskin
Title CEO

Phone: Main 325-555-0147 & Direct xxxxxx
Fax xxxxx
dale.hoskin@pellorvh.example
382 Wimble Street Box 415
Wrenfield, Ardenia 76902

Font styles to use
Serif

Colors
f48340

Requirements
Must have
• Clean crisp lines and ability to modify names, titles and emails
• On the back "PellorValleyHospital.Example
Nice to have
• Needs to be in line with logo, which is a bit dated and not too appealing, but I'm hoping that the rest of the card can make up for that fact just a little bit.
• Hospital's colors are a copper brown, black and white
Should not have
• Shapes or anything distracting

```html
<!DOCTYPE html>
<html lang="en">
<head>
<meta charset="utf-8">
<title>Pellor Valley Hospital – Business Cards</title>
<link rel="stylesheet" href="https://fonts.googleapis.com/css2?family=Open+Sans:wght@400;600;700&display=swap">
<style>
  :root {
    --copper: #f48340;
    --ink: #1c1c1c;
    --paper: #ffffff;
    --backdrop: #3a3a3a;
    --card-dark-top: #333333;
    --card-dark-bottom: #161616;
  }
  * { box-sizing: border-box; margin: 0; padding: 0; }
  html, body {
    width: 1200px; height: 800px; overflow: hidden;
    background: var(--backdrop);
    font-family: "Open Sans", Arial, sans-serif;
  }
  .stage { position: relative; width: 1200px; height: 800px; }

  /* Back of card */
  .card-back {
    position: absolute; left: 600px; top: 60px;
    width: 520px; height: 297px;
    background: linear-gradient(160deg, var(--card-dark-top), var(--card-dark-bottom));
    box-shadow: 0 10px 30px rgba(0,0,0,.45);
  }
  .card-back .brand-name {
    position: absolute; left: 0; right: 0; top: 88px;
    color: var(--paper);
    font-weight: 700; font-size: 38px; line-height: 1.1;
    text-align: center;
  }
  .card-back .website {
    position: absolute; left: 0; right: 0; bottom: 30px;
    text-align: center;
    font-size: 14px; letter-spacing: 2px; color: var(--paper);
  }
  .card-back .website .domain { color: var(--copper); }

  /* Front of card */
  .card-front {
    position: absolute; left: 80px; top: 390px;
    width: 640px; height: 366px;
    background: var(--paper);
    box-shadow: 0 10px 30px rgba(0,0,0,.45);
    border-bottom: 8px solid var(--copper);
  }
  .card-front .brand-name {
    position: absolute; left: 36px; top: 88px; width: 250px;
    color: var(--ink); font-weight: 700; font-size: 36px; line-height: 1.12;
  }
  .card-front .divider {
    position: absolute; left: 300px; top: 62px;
    width: 2px; height: 170px; background: var(--copper);
  }
  .contact { position: absolute; left: 322px; top: 62px; color: var(--ink); }
  .contact .person-name {
    color: var(--copper); font-weight: 700; font-size: 24px; line-height: 1.1;
  }
  .contact .person-title { font-size: 15px; margin: 2px 0 10px; }
  .contact ul { list-style: none; }
  .contact li {
    display: flex; align-items: center; gap: 10px;
    font-size: 16px; line-height: 23px; white-space: nowrap;
  }
  .contact li svg { width: 14px; height: 14px; fill: var(--copper); flex: none; }
  .card-front .address {
    position: absolute; left: 0; right: 0; bottom: 24px;
    text-align: center; font-size: 17px; color: var(--ink);
  }
</style>
</head>
<body>
<main class="stage">

  <section class="card-back" aria-label="Business card back">
    <h2 class="brand-name">Pellor Valley<br>Hospital</h2>
    <p class="website">www.<span class="domain">PellorValleyHospital</span>.Example</p>
  </section>

  <section class="card-front" aria-label="Business card front">
    <h1 class="brand-name">Pellor Valley Hospital</h1>
    <div class="divider"></div>
    <div class="contact">
      <p class="person-name">Marisol Keane</p>
      <p class="person-title">Doctor</p>
      <ul>
        <li>
          <svg viewBox="0 0 24 24" aria-hidden="true"><path d="M6.6 10.8a15.1 15.1 0 0 0 6.6 6.6l2.2-2.2c.3-.3.7-.4 1-.2 1.1.4 2.3.6 3.6.6.6 0 1 .4 1 1V20c0 .6-.4 1-1 1A17 17 0 0 1 3 4c0-.6.4-1 1-1h3.5c.6 0 1 .4 1 1 0 1.3.2 2.5.6 3.6.1.3 0 .7-.2 1z"/></svg>
          (555) 555-0147
        </li>
        <li>
          <svg viewBox="0 0 24 24" aria-hidden="true"><path d="M7 3h10v4H7zM4 8h16c1.1 0 2 .9 2 2v6h-4v5H6v-5H2v-6c0-1.1.9-2 2-2zm4 8v3h8v-3z"/></svg>
          (555) 555-0188
        </li>
        <li>
          <svg viewBox="0 0 24 24" aria-hidden="true"><path d="M2 5h20v14H2zm2 2v.5l8 5 8-5V7l-8 5z"/></svg>
          info@PellorValleyHospital.Example
        </li>
        <li>
          <svg viewBox="0 0 24 24" aria-hidden="true"><path d="M12 2a10 10 0 1 0 0 20 10 10 0 0 0 0-20zm6.9 6h-3a15 15 0 0 0-1.3-3.9A8 8 0 0 1 18.9 8zM12 4c.8 1.2 1.5 2.5 1.9 4h-3.8c.4-1.5 1.1-2.8 1.9-4zM4.3 14a8 8 0 0 1 0-4h3.4a16 16 0 0 0 0 4zm.8 2h3a15 15 0 0 0 1.3 3.9A8 8 0 0 1 5.1 16zM8 8H5.1a8 8 0 0 1 4.3-3.9C8.8 5.3 8.4 6.6 8 8zm4 12c-.8-1.2-1.5-2.5-1.9-4h3.8c-.4 1.5-1.1 2.8-1.9 4zm2.3-6H9.7a14 14 0 0 1 0-4h4.6a14 14 0 0 1 0 4zm.3 5.9c.6-1.2 1-2.5 1.3-3.9h3a8 8 0 0 1-4.3 3.9zm1.7-5.9a16 16 0 0 0 0-4h3.4a8 8 0 0 1 0 4z"/></svg>
          www.PellorValleyHospital.Example
        </li>
      </ul>
    </div>
    <p class="address">382 Wimble St., Wrenfield, Ardenia 76902</p>
  </section>

</main>
</body>
</html>
```